Flyer for spiritual retreat (yoga, meditation, reiki, raw food)

I would like a flyer to promote my upcoming retreat and a matching Facebook banner.

The name of the retreat is "Wavecrest Of Calm" and the tagline is "retreat into you"

The activities in the retreat include daily meditation, ecstatic dance, spiritual development workshops on intuition, energy healing etc and a reiki session is included.

I would like a flyer designed to promote this, something that is editable as I will be running this multiple times and will need to adjust the flyer to add the dates etc each time.

edit: add that here will be fully catered raw food and juices, and that the retreat price includes all accomodation, meals and workshops.

Please contact me if you need further info. Please also visit my website www.marithovland.com and www.facebook.com/tolvanahaven to see my current events and promotions.

Thank you,

Marit

Reason: Hi all, thank you all for your submissions. Apologies as I am traveling and do not have much access to internet and will review your submissions and provide feedback as soon as possible. Kind regards, Marit.

Target Market(s)

People who like meditation, yoga, fans of rowan mabry and jasper vinek, those interested in personal and spiritual development.

Industry/Entity Type

Health And Wellness

Requirements
Must have
• Please put the included reiki session as as added bonus. Something like "BONUS 30 minute reiki healing session" in a little star/banner/something that stands out.
• Please emphasise the "light" part of Wavecrest as I am going for a play on words between in the light and enlightenment.
• Please include placeholder text for place, location, time
• Placeholder for price
• My name (see attached file - can change colour to suit) and website (www.marithovland.com)
Nice to have
• I prefer rounded designs, curves rather than block designs.
Should not have
• Tolvana Haven logo

```html
<!DOCTYPE html>
<html lang="en">
<head>
<meta charset="utf-8">
<title>Wavecrest Of Calm – Retreat Flyer</title>
<link href="https://fonts.googleapis.com/css2?family=Questrial&family=Caveat:wght@700&family=Open+Sans:wght@400;600;700&family=Great+Vibes&display=swap" rel="stylesheet">
<style>
  :root {
    --sky: #cfe9f3;
    --ink: #1d1d1f;
    --tagline: #3c5fae;
    --rose: #d4837d;
    --mauve: #a79ea7;
    --slate: #8aa7b4;
    --aqua: #b5dee1;
    --bonus: #e47d78;
    --footer: #3cb6e6;
    --line: rgba(255,255,255,.9);
  }
  * { margin: 0; padding: 0; box-sizing: border-box; }
  html, body { width: 849px; height: 1200px; overflow: hidden; background: var(--sky); }
  .flyer { position: relative; width: 849px; height: 1200px; background: var(--sky); font-family: "Open Sans", sans-serif; color: var(--ink); }

  .header { position: absolute; left: 0; top: 0; width: 849px; height: 182px; background: var(--sky); }
  .header__figure { position: absolute; left: 8px; top: 10px; width: 190px; height: 170px;
    background: radial-gradient(ellipse 55% 50% at 45% 58%, rgba(79,134,200,.85) 0%, rgba(127,176,224,.6) 50%, rgba(207,233,243,0) 100%); }
  .header__foliage { position: absolute; right: 0; top: 0; width: 150px; height: 165px;
    background: radial-gradient(ellipse 60% 55% at 65% 45%, rgba(255,255,255,.6) 0%, rgba(255,255,255,.2) 55%, rgba(207,233,243,0) 100%); }
  .header__title { position: absolute; left: 0; right: 0; top: 14px; text-align: center;
    font-family: "Questrial", sans-serif; font-weight: 400; font-size: 45px; letter-spacing: .5px; color: var(--ink); }
  .header__title .light { color: var(--tagline); }
  .header__tagline { position: absolute; left: 0; right: 0; top: 82px; text-align: center;
    font-family: "Caveat", cursive; font-weight: 700; font-size: 62px; color: var(--tagline); letter-spacing: 3px; }

  .hero { position: absolute; left: 0; top: 182px; width: 849px; height: 546px;
    background:
      linear-gradient(to bottom, rgba(52,42,26,0) 0%, rgba(52,42,26,0) 60%, rgba(72,58,34,.55) 74%, rgba(52,42,26,.92) 92%, #3a2f1e 100%),
      radial-gradient(ellipse 40% 30% at 52% 48%, rgba(255,255,250,.95) 0%, rgba(255,250,232,0) 100%),
      radial-gradient(ellipse 70% 60% at 50% 42%, #fffaf0 0%, #f8e9c0 40%, #e9cf8f 75%, #c9a866 100%); }

  .panel { position: absolute; }
  .icon-frame { position: absolute; border: 2px solid var(--line); border-radius: 50%; }

  .activities { left: 0; top: 740px; width: 424px; height: 217px; background: var(--rose); }
  .activities__icon { left: 30px; top: 46px; width: 118px; height: 118px; }
  .activities__list { position: absolute; left: 162px; top: 46px; list-style: none;
    font-weight: 700; font-size: 16.5px; line-height: 24px; color: var(--ink); }
  .activities__list li { padding-left: 14px; text-indent: -14px; }
  .activities__list li::before { content: "•"; display: inline-block; width: 14px; text-indent: 0; }

  .details { left: 424px; top: 740px; width: 425px; height: 217px; background: var(--mauve); }
  .details__icon { left: 12px; top: 82px; width: 46px; height: 46px; }
  .details__note { position: absolute; left: 70px; top: 18px; width: 320px; text-align: center;
    font-size: 16px; line-height: 24px; color: var(--ink); }
  .details__price { position: absolute; left: 70px; width: 297px; top: 108px; text-align: center;
    font-weight: 700; font-size: 18px; }
  .details__address { position: absolute; left: 70px; top: 144px; width: 297px; text-align: center;
    font-size: 21px; line-height: 34px; color: var(--ink); }

  .bonus { left: 0; top: 957px; width: 424px; height: 198px; background: var(--slate); }
  .bonus__icon { left: 22px; top: 62px; width: 80px; height: 80px; }
  .bonus__label { position: absolute; left: 122px; top: 10px; font-weight: 700; font-size: 74px;
    line-height: 1; color: var(--bonus); }
  .bonus__length { position: absolute; left: 116px; top: 92px; font-size: 54px; line-height: 1; color: var(--ink); }
  .bonus__session { position: absolute; left: 118px; top: 144px; font-size: 27px; line-height: 1.2; color: var(--ink); }

  .host { left: 424px; top: 957px; width: 425px; height: 198px; background: var(--aqua); }
  .host__name { position: absolute; left: 0; right: 0; top: 50px; text-align: center;
    font-family: "Great Vibes", cursive; font-size: 60px; color: #2c2c2c; }

  .footer { position: absolute; left: 0; top: 1155px; width: 849px; height: 30px; background: var(--footer);
    text-align: center; font-size: 19px; line-height: 30px; letter-spacing: 1px; color: #2a3a44; }
</style>
</head>
<body>
<main class="flyer">
  <header class="header">
    <div class="header__figure" role="img" aria-label="Watercolour figure in a yoga pose with butterflies"></div>
    <div class="header__foliage" role="img" aria-label="White outline leaf sprigs"></div>
    <h1 class="header__title">Wave<span class="light">crest</span> Of Calm</h1>
    <p class="header__tagline">Retreat into you</p>
  </header>

  <section class="hero" role="img" aria-label="Woman meditating cross-legged in grass before sunlit water"></section>

  <section class="panel activities">
    <div class="icon-frame activities__icon" role="img" aria-label="Outline icon of a meditating figure"></div>
    <ul class="activities__list">
      <li>Daily Meditation</li>
      <li>Ecstatic Dance</li>
      <li>Spiritual Development Workshops on Intuition</li>
      <li>Energy Healing</li>
      <li>Reiki session is included</li>
    </ul>
  </section>

  <section class="panel details">
    <div class="icon-frame details__icon" role="img" aria-label="Outline lotus icon"></div>
    <p class="details__note">Fully catered raw food and juices, and that the retreat price includes all accomodation, meals and workshops.</p>
    <p class="details__price">P300</p>
    <p class="details__address">123 Lorem Ipsum<br>Incognito 32456</p>
  </section>

  <section class="panel bonus">
    <div class="icon-frame bonus__icon" role="img" aria-label="Outline lotus with radiating rays"></div>
    <p class="bonus__label">BONUS</p>
    <p class="bonus__length">30 minute</p>
    <p class="bonus__session">reiki healing session</p>
  </section>

  <section class="panel host">
    <p class="host__name">Marit Hovland</p>
  </section>

  <footer class="footer">www.marithovland.com</footer>
</main>
</body>
</html>
```